Alloy wheel repair business needs a website

Install logo previously purchased from pixelbazaar, toolbar with dropdowns. services, gallery, clients , contact ect
Maybe mission statment

Target Market(s)

vehicle owners, auto dealers,insurance companies,

Industry/Entity Type

Alloy Wheel Repair

Coding

Coded - Design and coding required

Number of Pages Required

4 page

Font styles to use
Sans Serif

Colors
0054AA
0677BA
7BADD7
CADEEF
E8F1F8

```html
<!DOCTYPE html>
<html lang="en">
<head>
<meta charset="utf-8">
<title>Rimcraft Wheel Co — Alloy Wheel Repair</title>
<link href="https://fonts.googleapis.com/css2?family=Michroma&family=Montserrat:wght@400;500;600;700&display=swap" rel="stylesheet">
<style>
:root{
  --blue-deep:#0054AA;
  --blue:#0677BA;
  --blue-mid:#7BADD7;
  --blue-soft:#CADEEF;
  --blue-pale:#E8F1F8;
  --ink:#1b1b1f;
  --text:#6f7480;
  --white:#ffffff;
  --black:#050505;
  --nav:#4a8fd0;
}
*{box-sizing:border-box;margin:0;padding:0}
html,body{width:1200px;height:5286px;overflow:hidden}
body{font-family:"Montserrat",sans-serif;color:var(--ink);background:var(--white);position:relative}
.abs{position:absolute}
.display{font-family:"Michroma",sans-serif;font-weight:400;letter-spacing:1px;text-transform:uppercase}
.section-title{position:absolute;left:0;width:1200px;text-align:center;font-size:28px;line-height:38px;color:var(--ink)}
.section-title .accent{color:var(--blue-deep)}
.lead{position:absolute;left:295px;width:610px;text-align:center;font-size:12.5px;line-height:20px;color:var(--text)}
.btn{position:absolute;display:flex;align-items:center;justify-content:center;background:var(--blue-deep);color:var(--white);font-size:11.5px;font-weight:600}

/* header */
.brand{left:160px;top:22px;font-size:18px;color:var(--blue-deep);display:flex;align-items:center;gap:10px}
.brand .dot{width:14px;height:14px;border-radius:50%;background:var(--blue-deep)}
.callout{left:695px;top:14px;display:flex;gap:12px;align-items:center}
.callout small{display:block;font-size:11px;color:var(--ink)}
.callout strong{display:block;font-size:19px;font-weight:700;letter-spacing:1px}
.socials-top{left:938px;top:20px;display:flex;gap:7px}
.socials-top span{width:28px;height:28px;border-radius:50%;border:1px solid #bfc4cc}
.socials-top span.on{background:var(--blue);border-color:var(--blue)}
.nav{left:0;top:72px;width:1200px;height:31px;background:var(--nav)}
.nav ul{list-style:none;display:flex;position:absolute;left:163px;top:0;height:31px;align-items:center;gap:47px}
.nav li{font-size:10px;color:var(--white);font-weight:500;letter-spacing:.4px}

/* hero */
.hero{left:0;top:103px;width:1200px;height:474px;background:radial-gradient(ellipse at 70% 30%,#4a4c52 0%,#26272b 45%,#0e0e10 100%)}
.hero-title{left:160px;top:235px;font-size:40px;line-height:54px;color:var(--white);font-style:italic}
.hero-sub{left:160px;top:352px;font-size:12px;color:var(--white)}
.hero-btn{left:160px;top:399px;width:172px;height:36px;background:var(--nav);font-size:10.5px;transform:skewX(-12deg)}
.hero-btn span{transform:skewX(12deg)}

/* feature cards */
.feature{top:673px;width:414px;height:245px}
.feature .photo{left:0;top:0;width:195px;height:245px}
.feature .panel{left:195px;top:16px;width:219px;height:212px;border:1px solid var(--blue-soft);border-left:none;padding:22px 0 0 18px}
.feature .panel small{font-size:12px;font-weight:600;display:block}
.feature .panel h3{font-size:20px;font-weight:500;margin-top:4px}
.feature .panel p{font-size:11px;line-height:20px;color:var(--text);margin-top:10px;width:180px}
.feature .panel .btn{position:static;width:98px;height:28px;margin-top:14px;font-size:10.5px}

/* services */
.services-bg{left:0;top:1015px;width:1200px;height:590px;background:var(--blue-pale);clip-path:polygon(0 0,100% 0,100% 84%,0 100%)}
.svc{top:1172px;width:158px;height:188px;background:var(--white);text-align:center;padding-top:20px}
.svc .ring{width:90px;height:90px;border-radius:50%;background:var(--blue-deep);margin:0 auto;display:flex;align-items:center;justify-content:center;box-shadow:0 0 0 4px var(--white),0 0 0 5px var(--blue-mid)}
.svc h4{font-size:15px;font-weight:500;line-height:21px;margin-top:18px}
.svc.active{background:var(--blue-deep);color:var(--white)}
.svc.active .ring{background:var(--white);box-shadow:0 0 0 4px var(--blue-deep),0 0 0 5px var(--blue-soft)}

/* gallery */
.compare{left:311px;top:1828px;width:578px;height:287px;background:linear-gradient(90deg,#3d4046 0%,#6d7077 35%,#8b8e94 55%,#42454b 100%)}
.compare .divider{left:288px;top:0;width:2px;height:287px;background:var(--white)}
.compare .knob{left:244px;top:120px;width:90px;height:46px;border-radius:23px;background:rgba(70,70,76,.85);display:flex;align-items:center;justify-content:center;gap:14px}
.compare .tag{top:136px;font-size:11px;color:var(--white);font-weight:500}
.thumb{top:2150px;width:204px;height:112px}

/* coloring */
.coloring-bg{left:0;top:2432px;width:1200px;height:580px;background:var(--blue-pale);clip-path:polygon(0 0,100% 0,100% 100%,0 90%)}
.car{top:2773px;width:204px;height:116px}

/* why */
.why-copy{left:160px;top:3170px;width:372px;font-size:11.5px;line-height:20px;color:var(--text)}
.why-copy p+p{margin-top:4px}
.play{left:318px;top:3362px;display:flex;align-items:center;gap:10px;font-size:12px;font-weight:600}
.play .circ{width:36px;height:36px;border-radius:50%;border:2px solid #e2e4ea;display:flex;align-items:center;justify-content:center}
.play .circ span{width:26px;height:26px;border-radius:50%;background:#e3101e;display:flex;align-items:center;justify-content:center}
.video{left:599px;top:3155px;width:439px;height:262px;background:linear-gradient(135deg,#3e4c63 0%,#23324f 40%,#5b2f33 100%)}
.video .bar{left:24px;bottom:14px;width:390px;height:4px;background:rgba(255,255,255,.35)}
.video .bar i{display:block;width:70px;height:4px;background:#e3101e}

/* everybody */
.everybody-bg{left:0;top:3515px;width:1200px;height:585px;background:var(--blue-pale)}
.aud{width:250px}
.aud h4{font-size:15px;font-weight:600}
.aud p{font-size:11.5px;line-height:18px;color:var(--text);margin-top:10px}
.aud.left{text-align:right}
.badge{width:62px;height:62px;border-radius:50%;background:var(--white);box-shadow:0 4px 14px rgba(0,84,170,.15);display:flex;align-items:center;justify-content:center}
.badge.solid{background:var(--blue-deep)}
.num{font-family:"Michroma",sans-serif;font-size:40px;color:var(--blue-soft)}
.product-photo{left:470px;top:3710px;width:260px;height:265px;background:linear-gradient(160deg,#dfe3e8 0%,#c9cdd3 45%,#d7aeb0 100%)}

/* reviews */
.review{top:4340px;width:272px;height:260px;background:var(--white);border:1px solid #e3e6ea;text-align:center}
.review .top{height:52px;border-bottom:1px solid #e3e6ea;position:relative}
.review .g{position:absolute;left:18px;top:16px;width:24px;height:24px;border-radius:50%;background:#e44235}
.review .stars{position:absolute;right:22px;top:18px;color:#f5a623;font-size:12px;letter-spacing:2px}
.review p{font-size:11.5px;line-height:22px;color:var(--text);padding:12px 20px 0}
.review .who{position:absolute;left:0;bottom:0;width:100%;height:76px;background:#f2f2f2;display:flex;align-items:center;gap:10px;padding-left:18px;text-align:left}
.review .avatar{width:54px;height:54px;border-radius:50%;background:radial-gradient(circle,#d9b9a5 0%,#a77b68 100%);border:3px solid var(--white)}
.review .who b{display:block;font-size:13px;font-weight:600}
.review .who span{font-size:11px}
.review.featured{top:4325px;background:var(--blue-deep);color:var(--white);border:none}
.review.featured .top{border-color:rgba(255,255,255,.25)}
.review.featured p{color:var(--white)}
.review.featured .who{background:var(--blue-mid);color:var(--white)}

/* footer */
.footer-bg{left:0;top:4780px;width:1200px;height:506px;background:var(--black);clip-path:polygon(0 19%,100% 0,100% 100%,0 100%)}
.footer h5{font-size:14px;font-weight:600;color:var(--white);letter-spacing:.5px}
.footer li,.footer p{font-size:11.5px;line-height:27px;color:var(--white);list-style:none}
.footer-brand{left:160px;top:4998px;width:180px;font-size:13px;line-height:18px;color:var(--white);display:flex;align-items:center;gap:8px}
.footer-brand .dot{width:12px;height:12px;border-radius:50%;background:var(--white);flex:none}
.footer .social{display:flex;gap:9px;margin-top:14px}
.footer .social span{width:28px;height:28px;background:var(--white)}
.contact-row{display:flex;gap:12px;margin-top:12px}
.contact-row p{line-height:19px}
.email-field{width:210px;height:36px;background:var(--white);font-size:11.5px;color:#555;padding:11px 12px}
.legal{top:5240px;font-size:11px;color:var(--white)}
</style>
</head>
<body>

<!-- header -->
<div class="abs brand display"><span class="dot"></span>Rimcraft Wheel Co</div>
<div class="abs callout">
  <svg width="40" height="40" viewBox="0 0 40 40" fill="none" stroke="#0677BA" stroke-width="2"><path d="M9 6c3 0 5 6 5 8s-4 3-4 5 5 9 9 11 4-3 6-3 6 3 6 5-2 5-5 5C16 37 4 24 4 12c0-3 3-6 5-6z"/></svg>
  <div><small>Call Us Today!</small><strong>555-014-2290</strong></div>
</div>
<div class="abs socials-top"><span></span><span class="on"></span><span></span></div>
<nav class="abs nav"><ul><li>WHEEL REPAIR SERVICES</li><li>WHEEL CUSTOM COLORING</li><li>ABOUT US</li><li>OUR GALLERY</li><li>LATEST BLOGS</li><li>RESOURCES</li><li>CONTACT US</li></ul></nav>

<!-- hero -->
<section class="abs hero" role="img" aria-label="Dark close-up photo of an alloy wheel"></section>
<h1 class="abs display hero-title">Alloy Wheel<br>Repair Service</h1>
<p class="abs hero-sub">Lorem Ipsum is simply dummy text of the printing and typesetting industry.</p>
<a class="btn hero-btn"><span>CONTACT US TODAY!</span></a>

<!-- feature cards -->
<div class="abs feature" style="left:160px">
  <div class="abs photo" role="img" aria-label="Technician repairing a wheel" style="background:linear-gradient(135deg,#2b2d33,#7c7f86 60%,#b02a2a)"></div>
  <div class="abs panel"><small>Wheel</small><h3>Repair Services</h3><p>Lorem ipsum dolor sit amet, consectetuer adipiscing elit, sed diam nonummy nibh</p><a class="btn">Read More</a></div>
</div>
<div class="abs feature" style="left:625px">
  <div class="abs photo" role="img" aria-label="Gold coloured custom alloy wheel" style="background:linear-gradient(135deg,#3a3328,#a8863f 55%,#2a2a2c)"></div>
  <div class="abs panel"><small>Wheel</small><h3>Custom Coloring</h3><p>Lorem ipsum dolor sit amet, consectetuer adipiscing elit, sed diam nonummy nibh</p><a class="btn">Read More</a></div>
</div>

<!-- services -->
<div class="abs services-bg"></div>
<svg class="abs" style="left:940px;top:1300px" width="260" height="262" viewBox="0 0 260 262"><polygon points="260,0 260,262 0,262" fill="#CADEEF"/><polygon points="260,60 260,262 60,262" fill="#b7d1ea" opacity=".6"/></svg>
<h2 class="section-title display" style="top:1110px"><span class="accent">Rimcraft</span> Wheel Services</h2>

<svg width="0" height="0" style="position:absolute"><defs>
  <symbol id="wheel" viewBox="0 0 48 48"><g fill="none" stroke="currentColor" stroke-width="2"><circle cx="24" cy="24" r="20"/><circle cx="24" cy="24" r="13"/><circle cx="24" cy="24" r="4"/><path d="M24 11v9M24 28v9M11 24h9M28 24h9M15 15l6 6M27 27l6 6M33 15l-6 6M21 27l-6 6"/></g></symbol>
</defs></svg>

<div class="abs svc" style="left:160px"><div class="ring"><svg width="54" height="54" style="color:#fff"><use href="#wheel"/></svg></div><h4>Wheel<br>Refinishing</h4></div>
<div class="abs svc" style="left:340px"><div class="ring"><svg width="54" height="54" style="color:#fff"><use href="#wheel"/></svg></div><h4>Wheel<br>Straightening</h4></div>
<div class="abs svc active" style="left:520px"><div class="ring"><svg width="54" height="54" style="color:#0054AA"><use href="#wheel"/></svg></div><h4>Wheel<br>Remanufacturing</h4></div>
<div class="abs svc" style="left:700px"><div class="ring"><svg width="54" height="54" style="color:#fff"><use href="#wheel"/></svg></div><h4>Wheel<br>Custom Coloring</h4></div>
<div class="abs svc" style="left:880px"><div class="ring"><svg width="54" height="54" style="color:#fff"><use href="#wheel"/></svg></div><h4>OEM<br>Wheel Sales</h4></div>
<a class="btn" style="left:544px;top:1390px;width:112px;height:36px">View All</a>

<!-- gallery -->
<h2 class="section-title display" style="top:1656px"><span class="accent">Work</span> Gallery</h2>
<p class="lead" style="top:1706px">Lorem ipsum dolor sit amet, consectetuer adipiscing elit, sed diam nonummy nibh euismod tincidunt ut laoreet dolore magna aliquam erat volutpat. Ut wisi enim ad minim veniam, quis nostrud exerci tation ullamcorper suscipit lobortis nisl ut aliquip ex ea commodo consequat. Duis autem vel eum iriure dolor in hendrerit in vulputate velit esse molestie consequat.</p>
<svg class="abs" style="left:270px;top:1960px" width="32" height="24" viewBox="0 0 32 24" fill="none" stroke="#555" stroke-width="2"><path d="M30 12H3M12 3l-9 9 9 9"/></svg>
<svg class="abs" style="left:898px;top:1960px" width="32" height="24" viewBox="0 0 32 24" fill="none" stroke="#0054AA" stroke-width="2"><path d="M2 12h27M20 3l9 9-9 9"/></svg>
<div class="abs compare" role="img" aria-label="Before and after photo of a refurbished silver alloy wheel">
  <span class="abs tag" style="left:18px">BEFORE</span>
  <span class="abs tag" style="right:18px">AFTER</span>
  <div class="abs divider"></div>
  <div class="abs knob"><svg width="10" height="16" viewBox="0 0 10 16" fill="none" stroke="#bbb" stroke-width="2.5"><path d="M8 2 2 8l6 6"/></svg><svg width="10" height="16" viewBox="0 0 10 16" fill="none" stroke="#fff" stroke-width="2.5"><path d="M2 2l6 6-6 6"/></svg></div>
</div>
<div class="abs thumb" style="left:160px;background:linear-gradient(135deg,#1d1f24,#8e939a 55%,#2b2d31)" role="img" aria-label="Refinished multi-spoke wheel"></div>
<div class="abs thumb" style="left:385px;background:linear-gradient(135deg,#1b6a8a,#6b4fb8 50%,#151518)" role="img" aria-label="Wheel under coloured lights"></div>
<div class="abs thumb" style="left:610px;background:linear-gradient(135deg,#5c1012,#a8a9ad 50%,#7d1518)" role="img" aria-label="Chrome wheel on a red car"></div>
<div class="abs thumb" style="left:835px;background:linear-gradient(135deg,#9e1d22,#c49a55 55%,#2a2a2c)" role="img" aria-label="Gold accented wheel on a red car"></div>
<a class="btn" style="left:513px;top:2295px;width:174px;height:36px">Get Wheel Repair Help</a>

<!-- custom coloring -->
<div class="abs coloring-bg"></div>
<svg class="abs" style="left:0;top:2715px" width="256" height="260" viewBox="0 0 256 260"><polygon points="0,0 256,260 0,260" fill="#CADEEF"/><polygon points="0,60 196,260 0,260" fill="#b7d1ea" opacity=".6"/></svg>
<h2 class="section-title display" style="top:2522px"><span class="accent">Wheel</span><br>Custom Coloring</h2>
<p class="lead" style="top:2610px">Lorem ipsum dolor sit amet, consectetuer adipiscing elit, sed diam nonummy nibh euismod tincidunt ut laoreet dolore magna aliquam erat volutpat. Ut wisi enim ad minim veniam, quis nostrud exerci tation ullamcorper suscipit lobortis nisl ut aliquip ex ea commodo consequat.</p>
<a class="btn" style="left:543px;top:2697px;width:116px;height:36px">See Our Gallery</a>
<div class="abs car" style="left:160px;background:linear-gradient(160deg,#2a2a2e,#b3141b 55%,#3a0a0c)" role="img" aria-label="Red sports car"></div>
<div class="abs car" style="left:385px;background:linear-gradient(160deg,#8fa3a0,#1d6b54 55%,#2f3a38)" role="img" aria-label="Green SUV"></div>
<div class="abs car" style="left:610px;background:linear-gradient(160deg,#e9ecef,#b9bec4 55%,#6f747a)" role="img" aria-label="White sports car"></div>
<div class="abs car" style="left:835px;background:linear-gradient(160deg,#a7b6c9,#8a4a25 55%,#4b3a2c)" role="img" aria-label="Orange off-road truck"></div>

<!-- why choose -->
<h2 class="section-title display" style="top:3050px"><span class="accent">Why Choose</span><br>Rimcraft Wheel Co</h2>
<div class="abs why-copy">
  <p>Lorem ipsum dolor sit amet, consectetuer adipiscing elit, sed diam nonummy nibh euismod tincidunt ut laoreet dolore magna aliquam erat volutpat. Ut wisi enim ad minim veniam, quis nostrud exerci tation ullamcorper suscipit lobortis nisl ut aliquip ex ea commodo consequat.</p>
  <p>Duis autem vel eum iriure dolor in hendrerit in vulputate velit esse molestie consequat, vel illum dolore eu feugiat nulla facilisis at vero eros et accumsan et iusto odio.</p>
</div>
<a class="btn" style="left:160px;top:3362px;width:143px;height:36px">Contact Us Today</a>
<div class="abs play"><div class="circ"><span><svg width="10" height="12" viewBox="0 0 10 12"><path d="M1 1l8 5-8 5z" fill="#fff"/></svg></span></div>Play Video</div>
<svg class="abs" style="left:385px;top:3360px" width="200" height="40" viewBox="0 0 200 40" fill="none" stroke="#c9ccd3" stroke-dasharray="3 4"><path d="M0 30c50 10 120 10 200-28"/></svg>
<div class="abs video" role="img" aria-label="Video still of two mechanics checking a car wheel">
  <div class="abs bar"><i></i></div>
</div>

<!-- everybody -->
<div class="abs everybody-bg"></div>
<svg class="abs" style="left:940px;top:3840px" width="260" height="262" viewBox="0 0 260 262"><polygon points="260,0 260,262 0,262" fill="#CADEEF"/><polygon points="260,60 260,262 60,262" fill="#b7d1ea" opacity=".6"/></svg>
<h2 class="section-title display" style="top:3606px"><span class="accent">Everybody Is Our Customer</span><br>At Rimcraft Wheel Co</h2>

<div class="abs aud left" style="left:75px;top:3738px;width:260px"><h4>Retail Sales</h4><p>Lorem ipsum dolor sit amet, consectetuer adipiscing elit, sed diam nonummy nibh.</p></div>
<div class="abs num" style="left:405px;top:3712px">1</div>
<div class="abs badge" style="left:355px;top:3740px"><svg width="34" height="34" style="color:#8a8f99"><use href="#wheel"/></svg></div>
<div class="abs aud left" style="left:75px;top:3862px;width:260px"><h4>Wholesale</h4><p>Lorem ipsum dolor sit amet, consectetuer adipiscing elit, sed diam nonummy nibh.</p></div>
<div class="abs num" style="left:405px;top:3836px">2</div>
<div class="abs badge" style="left:355px;top:3864px"><svg width="34" height="34" style="color:#8a8f99"><use href="#wheel"/></svg></div>

<div class="abs product-photo" role="img" aria-label="Photo of red and chrome alloy wheels"></div>

<div class="abs num" style="left:757px;top:3712px">3</div>
<div class="abs badge solid" style="left:780px;top:3740px"><svg width="34" height="34" style="color:#fff"><use href="#wheel"/></svg></div>
<div class="abs aud" style="left:862px;top:3738px"><h4>Join Our Team</h4><p>Lorem ipsum dolor sit amet, consectetuer adipiscing elit, sed diam nonummy nibh.</p></div>
<div class="abs num" style="left:757px;top:3836px">4</div>
<div class="abs badge" style="left:780px;top:3864px"><svg width="34" height="34" style="color:#8a8f99"><use href="#wheel"/></svg></div>
<div class="abs aud" style="left:862px;top:3862px"><h4>Buy OEM Wheels</h4><p>Lorem ipsum dolor sit amet, consectetuer adipiscing elit, sed diam nonummy nibh.</p></div>

<!-- reviews -->
<h2 class="section-title display" style="top:4190px"><span class="accent">What Our</span><br>Customers Say</h2>
<svg class="abs" style="left:116px;top:4490px" width="32" height="24" viewBox="0 0 32 24" fill="none" stroke="#555" stroke-width="2"><path d="M30 12H3M12 3l-9 9 9 9"/></svg>
<svg class="abs" style="left:1052px;top:4490px" width="32" height="24" viewBox="0 0 32 24" fill="none" stroke="#0054AA" stroke-width="2"><path d="M2 12h27M20 3l9 9-9 9"/></svg>

<div class="abs review" style="left:160px">
  <div class="top"><span class="g"></span><span class="stars">★★★★★</span></div>
  <p>Lorem ipsum dolor sit amet, consectetuer adipiscing elit, sed diam nonummy nibh euismod tincidunt ut laoreet dolore magna aliquam erat volutpat. Ut wisi enim ad minim.</p>
  <div class="who"><div class="avatar" role="img" aria-label="Customer portrait"></div><div><b>Nora T.</b><span>Lorem ipsum</span></div></div>
</div>
<div class="abs review featured" style="left:465px">
  <div class="top"><span class="g"></span><span class="stars">★★★★★</span></div>
  <p>Lorem ipsum dolor sit amet, consectetuer adipiscing elit, sed diam nonummy nibh euismod tincidunt ut laoreet dolore magna aliquam erat volutpat. Ut wisi enim ad minim.</p>
  <div class="who"><div class="avatar" role="img" aria-label="Customer portrait"></div><div><b>Dana Whitfield</b><span>Lorem ipsum</span></div></div>
</div>
<div class="abs review" style="left:768px">
  <div class="top"><span class="g"></span><span class="stars">★★★★★</span></div>
  <p>Lorem ipsum dolor sit amet, consectetuer adipiscing elit, sed diam nonummy nibh euismod tincidunt ut laoreet dolore magna aliquam erat volutpat. Ut wisi enim ad minim.</p>
  <div class="who"><div class="avatar" role="img" aria-label="Customer portrait"></div><div><b>Lena Ortiz</b><span>Lorem ipsum</span></div></div>
</div>
<a class="btn" style="left:544px;top:4680px;width:112px;height:36px">View All</a>

<!-- footer -->
<footer class="footer">
  <div class="abs footer-bg"></div>
  <svg class="abs" style="left:0;top:4812px" width="256" height="258" viewBox="0 0 256 258"><polygon points="0,0 256,0 0,258" fill="#0054AA"/><line x1="0" y1="250" x2="248" y2="0" stroke="#fff" stroke-width="2"/></svg>

  <div class="abs footer-brand display"><span class="dot"></span><span>Rimcraft<br>Wheel Co</span></div>
  <div class="abs" style="left:160px;top:5085px"><h5>FOLLOW US</h5><div class="social"><span></span><span></span><span></span><span></span></div></div>

  <div class="abs" style="left:362px;top:4992px"><h5>QUICK LINKS</h5>
    <ul style="margin-top:6px"><li>Home</li><li>Wheel Repair Services</li><li>Wheel Custom Coloring</li><li>Company Wheel Repair</li><li>Gallery</li><li>Contact Us</li></ul>
  </div>

  <div class="abs" style="left:565px;top:4992px"><h5>CONTACT DETAILS</h5>
    <div class="contact-row" style="margin-top:16px"><svg width="34" height="34" viewBox="0 0 34 34" fill="none" stroke="#fff" stroke-width="1.6"><path d="M4 16 17 5l13 11M8 13v16h18V13"/><circle cx="17" cy="19" r="3"/></svg><p>42 Orchard Lane<br>Springvale PA 10021</p></div>
    <div class="contact-row"><svg width="34" height="34" viewBox="0 0 34 34" fill="none" stroke="#fff" stroke-width="1.6"><path d="M8 5c3 0 4 5 4 7s-3 2-3 4 4 7 7 9 3-2 5-2 5 2 5 4-2 4-4 4C13 31 3 21 3 11c0-3 3-6 5-6z"/></svg><p>Phone<br>555-014-2290</p></div>
    <div class="contact-row"><svg width="34" height="34" viewBox="0 0 34 34" fill="none" stroke="#fff" stroke-width="1.6"><circle cx="17" cy="17" r="13"/><rect x="10" y="12" width="14" height="10"/><path d="M10 12l7 6 7-6"/></svg><p>Email<br>hello@rimcraftwheel.co</p></div>
  </div>

  <div class="abs" style="left:828px;top:4992px"><h5>NEWSLETTER SIGN UP</h5>
    <p style="line-height:19px;margin-top:10px">Subscribe to our newsletter to get<br>the latest update to your inbox</p>
    <div class="email-field" style="margin-top:14px">Email address</div>
    <div class="btn" style="position:static;width:142px;height:36px;margin-top:14px;font-size:13px;letter-spacing:.5px">SUBSCRIBE</div>
  </div>

  <div class="abs" style="left:160px;top:5226px;width:878px;height:1px;background:#2b2b2b"></div>
  <p class="abs legal" style="left:160px">© 2023 Rimcraft Wheel Co. All Rights Reserved.</p>
  <p class="abs legal" style="left:805px">Privacy Policy | Accessibility Statement</p>
</footer>

</body>
</html>
```